Bright Current Electrical & Communications business card design

We would like a double sided business card that is different. Want it to be exciting and fun. Something that people keep rather then just throw it in the bin.
We have a logo that we want to put on one side of the business card and then the business information on the reverse side. Trying to go for a real professional style of business card

Target Market(s)

Electrical

Industry/Entity Type

Electrical

Contact Information for Business Card

Bright Current Electrical & Communications
Marcus Holloway
P: 0437 862 305
E: brightcurrent@mailbox-example.com.au
Lic No: 574106K
24/7

Font styles to use
Other font styles liked:
• Would like ideas

Requirements
Must have
• Our company logo (preferably on both sides) yellow needs to be incorporated somewhere. Business card card colours to match with logo. Maybe a small pop of colour
Nice to have
• Open to some design ideas

```html
<!DOCTYPE html>
<html lang="en">
<head>
<meta charset="utf-8">
<title>Bright Current Electrical &amp; Communications – Business Card</title>
<link rel="stylesheet" href="https://fonts.googleapis.com/css2?family=Chakra+Petch:wght@400;600;700&display=swap">
<style>
  :root {
    --backdrop: #8a8b8b;
    --card-front: #dcdde0;
    --card-back: #111111;
    --brand-grey: #6f6f70;
    --accent-yellow: #f2e71c;
    --ink-light: #f2f2f2;
    --rule: #e8e8e8;
  }
  * { margin: 0; padding: 0; box-sizing: border-box; }
  html, body {
    width: 1200px;
    height: 900px;
    overflow: hidden;
    background: var(--backdrop);
    font-family: "Chakra Petch", sans-serif;
  }
  .canvas {
    position: relative;
    width: 1200px;
    height: 900px;
  }
  .card {
    position: absolute;
    left: 321px;
    width: 507px;
    height: 290px;
  }
  .card--front {
    top: 119px;
    background: var(--card-front);
    display: flex;
    align-items: center;
    justify-content: center;
  }
  .company-name {
    color: var(--brand-grey);
    font-weight: 600;
    font-size: 21px;
    line-height: 1.25;
    letter-spacing: 1.5px;
    text-transform: uppercase;
    text-align: center;
  }
  .card--back {
    top: 471px;
    background: var(--card-back);
    color: var(--ink-light);
  }
  .availability-icon {
    position: absolute;
    left: 426px;
    top: 34px;
    width: 44px;
    height: 44px;
  }
  .holder-name {
    position: absolute;
    left: 41px;
    top: 150px;
    font-size: 23px;
    font-weight: 600;
    color: var(--accent-yellow);
  }
  .holder-role {
    position: absolute;
    left: 41px;
    top: 174px;
    font-size: 17px;
    font-weight: 400;
  }
  .divider {
    position: absolute;
    left: 41px;
    top: 201px;
    width: 430px;
    height: 1px;
    background: var(--rule);
  }
  .contact-list {
    position: absolute;
    left: 41px;
    top: 212px;
    list-style: none;
  }
  .contact-item {
    display: flex;
    align-items: center;
    height: 18px;
    font-size: 13px;
    letter-spacing: 0.4px;
  }
  .contact-item--phone { font-size: 15px; }
  .contact-icon {
    width: 13px;
    height: 13px;
    margin-right: 9px;
    flex: none;
  }
  .licence {
    position: absolute;
    right: 37px;
    top: 248px;
    font-size: 12px;
  }
</style>
</head>
<body>
<main class="canvas">
  <section class="card card--front" aria-label="Card front">
    <p class="company-name">Bright Current Electrical<br>&amp; Communications</p>
  </section>

  <section class="card card--back" aria-label="Card back">
    <svg class="availability-icon" viewBox="0 0 44 44" aria-label="Open 24/7">
      <circle cx="22" cy="22" r="19.5" fill="none" stroke="#f2f2f2" stroke-width="2.5"/>
      <path d="M22 9 V23 L15 30" fill="none" stroke="#f2f2f2" stroke-width="2.5" stroke-linecap="round" stroke-linejoin="round"/>
    </svg>

    <h1 class="holder-name">Marcus Holloway</h1>
    <p class="holder-role">CEO/Founder</p>
    <div class="divider"></div>

    <ul class="contact-list">
      <li class="contact-item contact-item--phone">
        <svg class="contact-icon" viewBox="0 0 16 16" aria-hidden="true">
          <path d="M3.5 1 L6 1.5 L7 5 L5.3 6.4 C6.2 8.3 7.7 9.8 9.6 10.7 L11 9 L14.5 10 L15 12.5 C15 13.9 13.9 15 12.5 15 C6.7 15 1 9.3 1 3.5 C1 2.1 2.1 1 3.5 1 Z" fill="#f2e71c"/>
        </svg>
        0437 862 305
      </li>
      <li class="contact-item">
        <svg class="contact-icon" viewBox="0 0 16 16" aria-hidden="true">
          <rect x="1" y="3" width="14" height="10" fill="#f2e71c"/>
          <path d="M1.5 3.5 L8 9 L14.5 3.5" fill="none" stroke="#111111" stroke-width="1.4"/>
        </svg>
        brightcurrent@mailbox-example.com.au
      </li>
      <li class="contact-item">
        <svg class="contact-icon" viewBox="0 0 16 16" aria-hidden="true">
          <circle cx="8" cy="8" r="7" fill="#f2e71c"/>
          <path d="M1 8 H15 M8 1 C5 4 5 12 8 15 M8 1 C11 4 11 12 8 15" fill="none" stroke="#111111" stroke-width="1"/>
        </svg>
        www.brightcurrent-example.com
      </li>
    </ul>

    <p class="licence">Lic No: 574106K</p>
  </section>
</main>
</body>
</html>
```